Bright Ridge Outreach for Open Kinship Studies, Inc needs business card with logo

Non profit substance abuse prevention organization needs a business card with logo. Our tagline is "Reach a Youth, Build a Future". The logo should communicate connection, engagement, life-saving, strength, safety and growth. The logo can be a symbol or the organization's name. Multi-color. Refer to our website BROOKSinc.example for more about our non-profit.

Branding BROOKS is very important. Our tagline is "Reach a Youth, Build a Future"

Thank you

Target Market(s)

Our target clients are corporate sponsors, local/state/federal grantors, parents, community leaders, professional counselors, doctors, therapists

Industry/Entity Type

Safety

Logo Text

Logo can be a graphic design symbol, BROOKS, inc. or Bright Ridge Outreach for Open Kinship Studies, Inc.

Requirements
Nice to have
• The acronym BROOKS inc in the design would be great. We are new so starting with a symbol might not work to get the branded name out to the public.

View website.....brooksinc.example

```html
<!DOCTYPE html>
<html lang="en">
<head>
<meta charset="utf-8">
<title>BROOKS business card</title>
<link rel="stylesheet" href="https://fonts.googleapis.com/css2?family=PT+Sans:wght@400;700&family=PT+Sans+Narrow:wght@400;700&display=swap">
<style>
  :root{
    --bg:#4a3a4a;
    --card:#fcfde6;
    --purple:#7548b6;
    --purple-soft:#a98ddc;
    --green:#4cc23a;
    --green-text:#3a9f2e;
    --green-pale:#d9f2c4;
  }
  *{box-sizing:border-box;margin:0;padding:0}
  html,body{width:1200px;height:800px;overflow:hidden}
  body{
    background:var(--bg);
    font-family:"PT Sans",sans-serif;
    display:flex;flex-direction:column;align-items:center;justify-content:space-evenly;
  }
  .card{
    position:relative;width:640px;height:366px;background:var(--card);
    box-shadow:0 6px 18px rgba(0,0,0,.35);overflow:hidden;
  }
  .band{position:absolute;left:0;right:0;background:var(--purple)}
  .band--top{top:0;height:26px}
  .band--bottom{bottom:0;height:38px}

  /* front */
  .front .web{
    position:absolute;top:0;right:22px;height:26px;line-height:26px;
    color:var(--green);font-size:13px;letter-spacing:.28em;text-transform:uppercase;
  }
  .front .mark{
    position:absolute;left:50%;top:70px;transform:translateX(-50%);
    display:flex;flex-direction:column;align-items:center;
  }
  .brand{display:flex;align-items:center;gap:12px}
  .brand-dot{width:22px;height:22px;border-radius:50%;background:var(--green)}
  .brand-name{font-weight:700;color:var(--purple);letter-spacing:.02em}
  .front .brand-name{font-size:76px;line-height:1}
  .hands{border-radius:40px;background:linear-gradient(90deg,var(--green-pale),#eef9dc)}
  .front .hands{width:170px;height:54px;margin-top:14px}
  .tagline{color:var(--purple);text-transform:uppercase;font-family:"PT Sans Narrow",sans-serif;white-space:nowrap}
  .front .tagline{font-size:13px;margin-top:10px;letter-spacing:.02em}
  .front .mission{
    position:absolute;bottom:0;left:22px;right:22px;height:38px;
    display:flex;align-items:center;
    color:var(--green);font-size:10px;text-transform:uppercase;letter-spacing:.05em;line-height:1.35;
  }

  /* back */
  .back .identity{position:absolute;left:34px;top:44px}
  .person{font-family:"PT Sans Narrow",sans-serif;font-weight:700;font-size:27px;color:var(--green-text);text-transform:uppercase;letter-spacing:-.01em;white-space:nowrap}
  .person .first{color:var(--purple)}
  .role{font-size:19px;color:var(--green-text);margin-top:2px}
  .org{font-size:19px;color:var(--purple);line-height:1.2;max-width:330px}
  .contacts{position:absolute;left:34px;top:210px;list-style:none}
  .contacts li{display:flex;align-items:center;gap:10px;height:19px}
  .label{
    width:34px;height:13px;background:var(--purple);color:#fff;
    font-size:8px;text-transform:uppercase;text-align:center;line-height:13px;letter-spacing:.05em;
  }
  .value{font-family:"PT Sans Narrow",sans-serif;font-size:15px;color:var(--green-text);white-space:nowrap}
  .back .mark{position:absolute;right:34px;top:150px;display:flex;flex-direction:column;align-items:center}
  .back .brand-name{font-size:46px;line-height:1}
  .back .brand-dot{width:16px;height:16px}
  .back .hands{width:110px;height:36px;margin-top:10px}
  .back .tagline{font-size:10px;margin-top:6px}
  .repeat{
    position:absolute;bottom:0;left:0;right:0;height:38px;
    display:flex;justify-content:space-around;align-items:center;
    color:var(--purple-soft);font-size:18px;letter-spacing:.04em;
  }
</style>
</head>
<body>

<section class="card front" aria-label="Card front">
  <div class="band band--top"></div>
  <div class="web">www.brooksinc.example</div>
  <div class="mark">
    <div class="brand"><span class="brand-dot"></span><span class="brand-name">BROOKS</span></div>
    <div class="hands" role="img" aria-label="Illustration of two reaching hands"></div>
    <div class="tagline">Reach a Youth, Build a Future</div>
  </div>
  <div class="band band--bottom"></div>
  <p class="mission">To support young people and their families through steady mentoring, open community programs and practical tools that strengthen healthy choices early on.</p>
</section>

<section class="card back" aria-label="Card back">
  <div class="band band--top"></div>
  <div class="identity">
    <h1 class="person"><span class="first">Dana</span> Whitfield Morrow LCSW</h1>
    <p class="role">President/CEO</p>
    <p class="org">Bright Ridge Outreach for Open Kinship Studies, Inc</p>
  </div>
  <ul class="contacts">
    <li><span class="label">Tel</span><span class="value">(555) 014-2290</span></li>
    <li><span class="label">Email</span><span class="value">board@brooksinc.example</span></li>
    <li><span class="label">Web</span><span class="value">www.brooksinc.example</span></li>
    <li><span class="label">Add</span><span class="value">48 Harbor Mill Lane, Fairview VA 20100</span></li>
  </ul>
  <div class="mark">
    <div class="brand"><span class="brand-dot"></span><span class="brand-name">BROOKS</span></div>
    <div class="hands" role="img" aria-label="Illustration of two reaching hands"></div>
    <div class="tagline">Reach a Youth, Build a Future</div>
  </div>
  <div class="band band--bottom"></div>
  <div class="repeat"><span>BROOKS</span><span>BROOKS</span><span>BROOKS</span><span>BROOKS</span><span>BROOKS</span><span>BROOKS</span></div>
</section>

</body>
</html>
```